Vantorix Business
Card and Letter Head
Creative Brief
Professional
Dalton Prewitt
Owner
7153 Hollow Creek Christiansted, St. Croix VI 00820
sales@vantorix.net
vantorix.net
Custom Integrator
ultimate digital experience

```html
<!DOCTYPE html>
<html lang="en">
<head>
<meta charset="utf-8">
<title>Vantorix Business Card</title>
<link href="https://fonts.googleapis.com/css2?family=Roboto:wght@400;500&display=swap" rel="stylesheet">
<style>
  :root {
    --page: #ffffff;
    --card-dark: #141414;
    --card-deep: #050505;
    --gold: #c9b86a;
    --gold-soft: #8f8450;
    --band-start: #2a2a1c;
    --band-end: #6d6a3e;
    --text-light: #f2f2f2;
    --text-muted: #b9b9b9;
  }
  * { margin: 0; padding: 0; box-sizing: border-box; }
  html, body { width: 1200px; height: 334px; overflow: hidden; background: var(--page); }
  body { font-family: "Roboto", Arial, sans-serif; position: relative; }

  .card {
    position: absolute; top: 0; width: 583px; height: 334px; overflow: hidden;
    background: radial-gradient(ellipse at 50% 45%, var(--card-dark) 0%, var(--card-deep) 80%);
  }
  .card--front { left: 0; }
  .card--back { left: 617px; }

  .name-band {
    position: absolute; top: 0; left: 0; width: 100%; height: 44px;
    background: linear-gradient(90deg, var(--band-start) 0%, var(--band-start) 45%, var(--band-end) 100%);
    text-align: right; padding: 6px 18px 0 0;
  }
  .holder-name { color: var(--gold); font-size: 16px; font-weight: 500; letter-spacing: 0.5px; text-transform: uppercase; }
  .holder-role { color: var(--text-light); font-size: 12px; text-transform: uppercase; letter-spacing: 0.5px; }

  .brand { position: absolute; left: 0; width: 100%; text-align: center; }
  .brand-dot { display: block; margin: 0 auto; border-radius: 50%; }
  .brand-name {
    display: block; font-size: 31px; font-weight: 400; letter-spacing: 1px;
    text-transform: uppercase; color: var(--text-light);
  }
  .card--front .brand { top: 125px; }
  .card--front .brand-dot { width: 70px; height: 70px; background: var(--gold-soft); margin-bottom: 16px; }
  .card--back .brand { top: 95px; }
  .card--back .brand-dot { width: 80px; height: 80px; background: #d9d9d9; margin-bottom: 20px; }

  .brand-rule { position: absolute; top: 259px; left: 0; width: 100%; height: 1px; background: var(--gold-soft); opacity: 0.6; }

  .contact {
    position: absolute; left: 10px; top: 293px; font-size: 11.5px; line-height: 17px;
    color: var(--text-muted); text-transform: uppercase; letter-spacing: 0.2px;
  }
  .contact .email { text-transform: uppercase; }

  .backdrop-art {
    position: absolute; inset: 0;
    background: radial-gradient(circle at 50% 40%, #2b2b2b 0%, #1b1b1b 45%, #0b0b0b 85%);
  }
</style>
</head>
<body>
  <section class="card card--front">
    <header class="name-band">
      <p class="holder-name">Dalton Prewitt</p>
      <p class="holder-role">Owner</p>
    </header>
    <div class="brand">
      <span class="brand-dot"></span>
      <span class="brand-name">Vantorix</span>
    </div>
    <div class="brand-rule"></div>
    <address class="contact">
      <p>Add: 7153 Hollow Creek Christiansted, St. Croix VI 00820 Ph: 340 555 0142</p>
      <p>Fax: 340 555 0187 Email: <span class="email">sales@vantorix.net</span> Web: vantorix.net</p>
    </address>
  </section>

  <section class="card card--back">
    <div class="backdrop-art" role="img" aria-label="Large faint decorative emblem artwork filling the card background"></div>
    <div class="brand">
      <span class="brand-dot"></span>
      <span class="brand-name">Vantorix</span>
    </div>
  </section>
</body>
</html>
```